Redo of existing website www.stonvira.example

I would like it to look like the newer style website, with large images, less text. clean and modern looking. The new design should focus on call to action. ultimately that's what were looking for.Some features I would like to see we try to do good job of keeping up with our blog, and it is a good source of recent pictures of our work. I like four visitors to get the few pieces they're doing with a national brand or franchise pray. I like to stay far from the idea of a local one-man band with magnetic signs on his truck.
I think that clean beautiful images have the biggest impact. In my opinion most people don't read more than a couple lines of text. The text is more for search engines.
we are currently in the process of revising our logo as well, I will upload those files when I get them.
Please feel free to use content and images from our current website www.stonvira.example. we can purchase professional stock images if needed.
1. large call to action with easy contact form.
2. Blog roll on front page to showcase our recent work.
2. All social connect buttons.
Check out our reviews on ratewell!
My current websites
Www.stonvira.example
https://social.example/profile/604918273655102938417/about
www.socialpage.example/stonvira
http://www.blogsite.example/blog/curbguardian
https://microblog.example/Stonvira
websites I like the way they look.
http://quillpost.example/
http://www.cartwell.example/
http://www.brennickpaving.example/
http://www.tarmacways.example/
http://curbandcoatingworks.example/
Hello all,
I have just uploaded some images of our company mascot "Curb Guardian" and our new logo.
Project Deadline Extended
Reason: Death in family. Finally back to work.
Target Market(s)
We have 2 main groups of customers commercial and residential.
Commercial customers are Property owners and managers, operators of multi location business, restaurant, supermarket, banks, and are best source for repeat business
for Residential customers we provide driveway repair and driveway paving services.
for residential customers I would like to encourge the submission or pictures with the inquiry for a quick quote. Residential customers are typically a one time job but are a good source of referrals
I like how this website separates residential and commercial
http://www.glintcoatonline.example
Call

```html
<!DOCTYPE html>
<html lang="en">
<head>
<meta charset="utf-8">
<title>Stonvira – Asphalt Paving</title>
<link href="https://fonts.googleapis.com/css2?family=Open+Sans:wght@300;400;600;700;800&display=swap" rel="stylesheet">
<style>
:root{
  --yellow:#efc81a;
  --black:#0b0b0b;
  --panel:#1b1b1b;
  --white:#ffffff;
  --text:#6f6f6f;
  --title:#1e1e1e;
  --light:#f1f1f1;
  --field:#f4f4f4;
}
*{margin:0;padding:0;box-sizing:border-box}
html,body{width:1200px;height:2359px;overflow:hidden;background:var(--white)}
body{position:relative;font-family:'Open Sans',Arial,sans-serif;color:var(--text)}
.abs{position:absolute}
.header-band{left:0;top:0;width:1200px;height:430px;background:var(--black)}
.brand{left:168px;top:24px;display:flex;align-items:center;gap:10px;color:var(--white);font-weight:600;font-size:26px;line-height:1}
.brand-mark{width:14px;height:14px;background:var(--yellow)}
.call{right:164px;top:40px;color:var(--white);font-weight:700;font-size:17px;white-space:nowrap}
.main-nav{left:165px;top:77px;width:870px;height:58px;background:var(--yellow);display:flex;align-items:center;justify-content:space-between;padding:0 32px 0 29px}
.main-nav a{color:var(--white);font-weight:700;font-size:17px;text-decoration:none;white-space:nowrap}
.hero-photo{left:165px;top:151px;width:592px;height:338px;background:linear-gradient(180deg,#3d6fc4 0%,#6c94d4 40%,#b9b6ae 62%,#6f6a62 100%)}
.hero-caption{left:179px;top:241px;width:320px;height:207px;background:rgba(20,20,20,.82);padding:14px 14px}
.hero-caption h2{color:var(--yellow);font-size:24px;font-weight:700;line-height:1.1}
.hero-caption p{color:var(--white);font-size:13px;line-height:20px;margin-top:8px}
.btn-hero{left:195px;top:344px;width:261px;height:59px;background:var(--yellow);color:var(--title);font-weight:700;font-size:20px;display:flex;align-items:center;justify-content:center}
.dots{left:183px;top:458px;display:flex;gap:4px}
.dots span{width:9px;height:9px;border-radius:50%;background:#222}
.dots span:first-child{background:var(--yellow)}
.quick{left:757px;top:151px;width:278px;height:338px;background:var(--panel)}
.quick h3{position:absolute;left:14px;top:24px;color:var(--white);font-weight:400;font-size:16px}
.field{left:771px;width:251px;height:30px;background:var(--field);font-size:10px;color:#aaa;padding:8px 6px}
.btn-submit{left:771px;top:421px;width:86px;height:30px;background:var(--yellow);color:var(--white);font-weight:700;font-size:12px;display:flex;align-items:center;justify-content:center}
.split{left:165px;top:521px}
.split h2{position:absolute;font-weight:300;font-size:40px;line-height:1;white-space:nowrap}
.split p{position:absolute;font-size:12.5px;line-height:22px;width:370px}
.btn-small{height:28px;font-weight:700;font-size:12px;display:flex;align-items:center;justify-content:center}
.split .btn-small{position:absolute}
.section-title{color:var(--yellow);font-weight:400;font-size:22px}
.post-date{left:165px;width:64px;height:51px;background:var(--yellow);text-align:center;color:var(--white)}
.post-date b{display:block;font-size:24px;line-height:30px;font-weight:700}
.post-date small{display:block;font-size:11px;color:var(--title);line-height:14px}
.post-title{left:236px;color:var(--title);font-weight:700;font-size:21px;white-space:nowrap}
.post-meta{left:236px;font-size:12px;white-space:nowrap}
.post-photo{left:165px;width:241px;height:258px}
.post-lead{left:417px;width:315px;color:#444;font-weight:600;font-size:14px;line-height:24px}
.post-body{left:417px;width:315px;font-size:12.5px;line-height:22px}
.share-bar{left:165px;width:573px;height:49px;background:var(--light)}
.shares{position:absolute;left:13px;top:16px;display:flex;gap:4px}
.shares span{height:19px;padding:0 6px;border:1px solid #c9c9c9;background:#fafafa;font-size:10px;color:#3b5a8c;line-height:17px;font-weight:600}
.shares span.dark{background:#3a5574;color:var(--white);border-color:#3a5574}
.btn-read{position:absolute;right:10px;top:8px;width:88px;height:33px;background:var(--yellow);color:var(--white);font-weight:700;font-size:11px;display:flex;align-items:center;justify-content:center}
.search{left:755px;top:838px;width:278px;height:52px;background:var(--light);font-size:13px;font-weight:600;color:#555;padding:18px 14px}
.recent-photo{left:757px;top:978px;width:276px;height:175px;background:linear-gradient(160deg,#8fc04a 0%,#6f9a3a 45%,#9a9a94 70%,#7a9f46 100%)}
.side-block{left:755px;top:1162px;width:280px}
.side-text{font-size:12px;line-height:22px}
.side-block .btn-small{margin-top:10px;width:88px;height:32px;background:var(--yellow);color:var(--white);font-size:11px}
.social{left:757px;top:1505px;display:flex;gap:4px}
.social span{width:36px;height:36px;border-radius:50%}
.pager{left:165px;top:2197px;display:flex;gap:10px;align-items:center}
.pager span{width:24px;height:24px;border:1px solid #ccc;font-size:10px;color:#555;display:flex;align-items:center;justify-content:center;background:#fff}
.pager span.on{background:#333;color:#fff;border-color:#333}
.pager i{font-style:normal;font-size:12px;color:#555;width:14px;text-align:center}
.footer{left:0;top:2254px;width:1200px;height:105px;background:var(--black);color:var(--white);text-align:center}
.footer nav{padding-top:17px;font-size:16px}
.footer nav a{color:var(--white);text-decoration:none}
.footer nav em{font-style:normal;margin:0 22px}
.footer p{font-size:15px;margin-top:14px}
</style>
</head>
<body>
<div class="abs header-band"></div>
<div class="abs brand"><span class="brand-mark"></span>Stonvira</div>
<div class="abs call">Call Us Free: (555) 014-2290</div>
<nav class="abs main-nav">
  <a>Home</a><a>Commercial</a><a>Residential</a><a>About Us</a><a>Free Estimate</a><a>Testimonials</a><a>Blog</a>
</nav>

<div class="abs hero-photo" role="img" aria-label="Paving crew repairing an asphalt driveway on a sunny winter day"></div>
<div class="abs hero-caption">
  <h2>Driveaways</h2>
  <p>Stonvira providecustom,high-Quality driveawaypaving to fit your needs and budget</p>
</div>
<div class="abs btn-hero">CONTACT US TODAY!</div>
<div class="abs dots"><span></span><span></span><span></span><span></span></div>

<div class="abs quick"><h3>Quick Contact</h3></div>
<div class="abs field" style="top:211px">Name</div>
<div class="abs field" style="top:252px">Company name</div>
<div class="abs field" style="top:291px">E-Mail</div>
<div class="abs field" style="top:335px">Phone</div>
<div class="abs field" style="top:379px">Message</div>
<div class="abs btn-submit">SUBMIT</div>

<section class="abs split">
  <svg width="870" height="276" style="position:absolute;left:0;top:0">
    <rect width="870" height="276" fill="#efc81a"/>
    <polygon points="0,0 384,0 472,276 0,276" fill="#0b0b0b"/>
  </svg>
  <svg width="40" height="40" viewBox="0 0 40 40" style="position:absolute;left:32px;top:26px" fill="#efc81a">
    <polygon points="20,2 2,16 38,16"/><rect x="6" y="16" width="28" height="20"/>
    <rect x="11" y="21" width="6" height="6" fill="#0b0b0b"/><rect x="23" y="21" width="6" height="6" fill="#0b0b0b"/><rect x="17" y="28" width="6" height="8" fill="#0b0b0b"/>
  </svg>
  <h2 style="left:80px;top:26px;color:var(--yellow)">Residentials</h2>
  <p style="left:36px;top:95px;color:var(--white)">Lorem Ipsum is simply dummy text of the printing and typesetting industry. Lorem Ipsum has been the industry's standard dummy text ever since the 1500s, when an unknown printer took a galley of type and scrambled it to make a type specimen book.</p>
  <div class="btn-small" style="left:36px;top:217px;width:85px;background:var(--yellow);color:var(--white)">READ MORE</div>
  <svg width="40" height="40" viewBox="0 0 40 40" style="position:absolute;left:480px;top:26px" fill="#0b0b0b">
    <polygon points="20,2 2,12 38,12"/><rect x="4" y="13" width="32" height="3"/>
    <rect x="7" y="18" width="4" height="14"/><rect x="15" y="18" width="4" height="14"/><rect x="22" y="18" width="4" height="14"/><rect x="29" y="18" width="4" height="14"/>
    <rect x="3" y="33" width="34" height="4"/>
  </svg>
  <h2 style="left:544px;top:26px;color:var(--black)">Commercial</h2>
  <p style="left:480px;top:95px;color:var(--white)">Lorem Ipsum is simply dummy text of the printing and typesetting industry. Lorem Ipsum has been the industry's standard dummy text ever since the 1500s, when an unknown printer took a galley of type and scrambled it to make a type specimen book.</p>
  <div class="btn-small" style="left:488px;top:217px;width:85px;background:var(--black);color:var(--white)">READ MORE</div>
</section>

<h2 class="abs section-title" style="left:165px;top:840px">Blog Posts</h2>

<div class="abs post-date" style="top:904px"><b>03</b><small>APR 2014</small></div>
<h3 class="abs post-title" style="top:902px">How Big is the dozer ?</h3>
<div class="abs post-meta" style="top:935px">Posted in Uncategorized &nbsp;|&nbsp; Leave a comment</div>
<div class="abs post-photo" style="top:975px;background:linear-gradient(135deg,#d9a428 0%,#b78a2a 40%,#5a5550 75%,#3d3a36 100%)" role="img" aria-label="Orange paving machine with a worker in a safety vest"></div>
<div class="abs post-lead" style="top:968px">Really big! A good friend and I at a Hollister Brothers auction Vegas 2009.</div>
<div class="abs post-body" style="top:1025px">Lorem Ipsum is simply dummy text of the printing and typesetting industry. Lorem Ipsum has been the industry's standard dummy text ever since the 1500s, when an unknown printer took a galley of type and scrambled it to make a type specimen book. It has survived not only five centuries, but also the leap into electronic typesetting, remaining essentially unchanged. It was popularised in the 1960s with the release of Typeline sheets ...</div>
<div class="abs share-bar" style="top:1255px"><div class="shares"><span>Like</span><span>Share</span><span>+1</span><span class="dark">Post +</span></div><div class="btn-read">Read More</div></div>

<div class="abs post-date" style="top:1335px"><b>03</b><small>APR 2014</small></div>
<h3 class="abs post-title" style="top:1333px">How Big is the dozer ?</h3>
<div class="abs post-meta" style="top:1366px">Posted in Uncategorized &nbsp;|&nbsp; Leave a comment</div>
<div class="abs post-photo" style="top:1406px;background:linear-gradient(180deg,#c8cfd6 0%,#a3a7a8 40%,#4a4642 75%,#2e2b28 100%)" role="img" aria-label="Asphalt truck at a paving job with a crew member in an orange hat"></div>
<div class="abs post-lead" style="top:1399px">Really big! A good friend and I at a Hollister Brothers auction Vegas 2009.</div>
<div class="abs post-body" style="top:1456px">Lorem Ipsum is simply dummy text of the printing and typesetting industry. Lorem Ipsum has been the industry's standard dummy text ever since the 1500s, when an unknown printer took a galley of type and scrambled it to make a type specimen book. It has survived not only five centuries, but also the leap into electronic typesetting, remaining essentially unchanged. It was popularised in the 1960s with the release of Typeline sheets ...</div>
<div class="abs share-bar" style="top:1686px"><div class="shares"><span>Like</span><span>Share</span><span>+1</span><span class="dark">Post +</span></div><div class="btn-read">Read More</div></div>

<div class="abs post-date" style="top:1767px"><b>03</b><small>APR 2014</small></div>
<h3 class="abs post-title" style="top:1765px">How Big is the dozer ?</h3>
<div class="abs post-meta" style="top:1798px">Posted in Uncategorized &nbsp;|&nbsp; Leave a comment</div>
<div class="abs post-photo" style="top:1838px;background:linear-gradient(180deg,#3f7ed0 0%,#8fb3e0 45%,#8b8c88 65%,#6f9a3a 100%)" role="img" aria-label="Freshly paved parking lot with a company yard sign"></div>
<div class="abs post-lead" style="top:1831px">Really big! A good friend and I at a Hollister Brothers auction Vegas 2009.</div>
<div class="abs post-body" style="top:1888px">Lorem Ipsum is simply dummy text of the printing and typesetting industry. Lorem Ipsum has been the industry's standard dummy text ever since the 1500s, when an unknown printer took a galley of type and scrambled it to make a type specimen book. It has survived not only five centuries, but also the leap into electronic typesetting, remaining essentially unchanged. It was popularised in the 1960s with the release of Typeline sheets ...</div>
<div class="abs share-bar" style="top:2118px"><div class="shares"><span>Like</span><span>Share</span><span>+1</span><span class="dark">Post +</span></div><div class="btn-read">Read More</div></div>

<div class="abs pager"><span>&lsaquo;</span><span>1</span><span>2</span><span>3</span><span class="on">4</span><span>5</span><i>····</i><span>15</span><span>30</span><span>45</span><span>&rsaquo;</span></div>

<div class="abs search">Search
  <svg width="24" height="24" viewBox="0 0 24 24" style="position:absolute;right:14px;top:14px" fill="none" stroke="#bbb" stroke-width="2"><circle cx="9" cy="9" r="6"/><line x1="13.5" y1="13.5" x2="21" y2="21"/></svg>
</div>
<h2 class="abs section-title" style="left:755px;top:925px">Our Recent Work</h2>
<div class="abs recent-photo" role="img" aria-label="Aerial view of a paved office parking lot surrounded by lawns"></div>
<div class="abs side-block">
  <p class="side-text">Lorem Ipsum is simply dummy text of the printing and typesetting industry. Lorem Ipsum has been the industry's standard dummy text ever since the 1500s, when an unknown printer took a galley of type and scrambled it to make a type specimen book. It has survived not only five centuries, but also the leap into electronic typesetting, remaining essentially unchanged. It was popularised in the 1960s with the release of</p>
  <div class="btn-small">Read More</div>
</div>
<h2 class="abs section-title" style="left:755px;top:1448px">Connect With Us</h2>
<div class="abs social">
  <span style="background:#35b3dd"></span><span style="background:#d8322a"></span><span style="background:#f07a1a"></span><span style="background:#f08a1d"></span><span style="background:#dc3b2c"></span><span style="background:#3b5998"></span>
</div>

<footer class="abs footer">
  <nav><a>Home</a><em>|</em><a>Commercial</a><em>|</em><a>Residential</a><em>|</em><a>About Us</a><em>|</em><a>Free Estimate</a><em>|</em><a>Testimonials</a><em>|</em><a>Blog</a></nav>
  <p>© Company Name ,All Rights Reserved</p>
</footer>
</body>
</html>
```